property maintenance company covering all trades Plumbing,heating ,electrical building carpentry

business cards

Target Market(s)

DOMESTIC HOUSEHOLDS

Industry/Entity Type

Property Maintenance

Contact Information for Business Card

dorian Fellowes
07841 305918
Brightwell Property Maintenace

Font styles to use
Sans Serif

Colors
eda3c7
d2a4cc
b7a5cd

```html
<!DOCTYPE html>
<html lang="en">
<head>
<meta charset="utf-8">
<title>Brightwell Property Maintenace – Business Cards</title>
<link href="https://fonts.googleapis.com/css2?family=Lato:wght@400;700&display=swap" rel="stylesheet">
<style>
  :root {
    --backdrop: #bdbdbd;
    --lilac-deep: #ae9bd0;
    --lilac-light: #d8c8f2;
    --pink: #eda3c7;
    --orchid: #d2a4cc;
    --violet-text: #a98fd6;
    --white: #ffffff;
  }
  * { box-sizing: border-box; margin: 0; padding: 0; }
  html, body { width: 1200px; height: 837px; overflow: hidden; }
  body {
    background: var(--backdrop);
    font-family: "Lato", sans-serif;
    position: relative;
  }
  .card {
    position: absolute;
    top: 264px;
    width: 540px;
    height: 309px;
    border-radius: 4px;
    overflow: hidden;
    background: linear-gradient(120deg, var(--lilac-deep) 0%, var(--lilac-light) 100%);
    box-shadow: 0 10px 24px rgba(0,0,0,0.18);
  }
  .card--front { left: 40px; }
  .card--back { left: 620px; }

  /* front */
  .front-band {
    position: absolute;
    left: 0; top: 48px;
    width: 270px; height: 196px;
    background: var(--white);
    border-radius: 0 98px 98px 0;
  }
  .brand-mark {
    position: absolute;
    display: flex; flex-direction: column; align-items: center; justify-content: center;
    gap: 8px;
    text-align: center;
  }
  .front-band .brand-mark { right: 10px; top: 10px; width: 176px; height: 176px; }
  .brand-dot {
    width: 26px; height: 26px; border-radius: 50%;
    border: 2px solid var(--pink);
  }
  .brand-name {
    color: var(--pink);
    font-weight: 400;
    font-size: 15px;
    letter-spacing: 1.5px;
    line-height: 1.3;
  }
  .front-company {
    position: absolute;
    right: 30px; bottom: 36px;
    color: var(--white);
    font-size: 22px;
    letter-spacing: 0.3px;
  }

  /* back */
  .back-band {
    position: absolute;
    left: 52px; right: 0; top: 90px;
    height: 190px;
    background: var(--white);
    border-radius: 95px 0 0 95px;
  }
  .back-band .brand-mark { left: 8px; top: 8px; width: 174px; height: 174px; }
  .contact {
    position: absolute;
    left: 230px; top: 30px;
  }
  .contact__name { color: var(--violet-text); font-size: 21px; font-weight: 700; }
  .contact__title { color: var(--pink); font-size: 15px; margin-bottom: 14px; }
  .contact__line {
    color: var(--violet-text); font-size: 14px; line-height: 1.45;
    display: flex; align-items: center; gap: 6px;
  }
  .contact__icon { width: 14px; height: 14px; flex: none; }
</style>
</head>
<body>
  <section class="card card--front">
    <div class="front-band">
      <div class="brand-mark">
        <span class="brand-dot"></span>
        <span class="brand-name">Brightwell<br>Property<br>Maintenace</span>
      </div>
    </div>
    <p class="front-company">Brightwell Property Maintenace</p>
  </section>

  <section class="card card--back">
    <div class="back-band">
      <div class="brand-mark">
        <span class="brand-dot"></span>
        <span class="brand-name">Brightwell<br>Property<br>Maintenace</span>
      </div>
      <div class="contact">
        <p class="contact__name">dorian Fellowes</p>
        <p class="contact__title">Chief Executive Officer</p>
        <p class="contact__line">0000 Youe Address,2nd Ste.</p>
        <p class="contact__line">Ashcombe, Texas 1234</p>
        <p class="contact__line">
          <svg class="contact__icon" viewBox="0 0 14 14" aria-hidden="true"><rect width="14" height="14" rx="2" fill="#eda3c7"/><path d="M4.5 3.5c-.6.6-.6 2 .8 3.8s3 2.8 3.9 2.3l.9-.9-1.5-1.3-.8.6c-.6-.2-1.6-1.3-1.8-1.9l.6-.8L5.4 3z" fill="#fff"/></svg>
          07841 305918
        </p>
        <p class="contact__line">
          <svg class="contact__icon" viewBox="0 0 14 14" aria-hidden="true"><rect width="14" height="14" rx="2" fill="#eda3c7"/><rect x="3" y="4" width="8" height="6" fill="none" stroke="#fff" stroke-width="1"/><path d="M3 4l4 3.2L11 4" fill="none" stroke="#fff" stroke-width="1"/></svg>
          your@brightwellmail.com
        </p>
      </div>
    </div>
  </section>
</body>
</html>
```